Summer Sunglass offer

Need a poster design for a spring / summer campaign. We are an opticians with good footfall. The design needs to be eye catching and aimed at 40 year old plus. The offer is Up to 50% off sunglass offer, t&c apply. (I have attached our last year campaign)
Also need a 2 sided A5 leaflet design (see attached)
I've uploaded a copy of our logo

A5 leaflet should read:

Grab a bargain on two great looks this summer Upto 50% off sunglasses
Look great and stay safe in the sun this summer

We want you to look great, feel fantastic and most of all stay safe in the sun this summer. That’s why we’re offering you 50% off prescription sunglasses with every complete pair of glasses you buy this summer or 25% off for prescription sunglasses with no other purchase.
Find you new summer looks from our gorgeous collection of frames in store. It matters to us that you look great in your new glasses as much as how well you see through them, so we’ll be on hand to help you find frames that suit you best.
What new looks will you go for? Smart or sassy? Formal or Fun? Whatever you’re in the mood for, you’ll find it in our collections this summer.
Call in today to find your new looks, and remember to bring your prescription if you don’t need an eye test.

Target Market(s)

40 + year old

Industry/Entity Type

Optician

Colors

Designer to choose colors to be used in the design.

Requirements
Must have
• Images, preferably a male and Female image

```html
<!DOCTYPE html>
<html lang="en">
<head>
<meta charset="utf-8">
<title>Summer Sunglasses Offer – Harwell Eyecare Centre</title>
<link href="https://fonts.googleapis.com/css2?family=Roboto+Condensed:wght@700&family=Lora:ital@1&family=Lustria&display=swap" rel="stylesheet">
<style>
  :root {
    --paper: #eeeef2;
    --steel-blue: #a0bfca;
    --coral: #ee6e45;
    --teal: #3fa4ad;
    --white: #ffffff;
    --denim: #8aa7c6;
    --denim-soft: #b9c9db;
    --mustard: #e8b45a;
  }
  * { margin: 0; padding: 0; box-sizing: border-box; }
  html, body { width: 933px; height: 1200px; overflow: hidden; background: var(--paper); }
  .poster { position: relative; width: 933px; height: 1200px; background: var(--paper); overflow: hidden; }

  .frame-line { position: absolute; background: var(--steel-blue); }
  .frame-left { left: 58px; top: 53px; width: 3px; height: 1078px; }
  .frame-right { left: 874px; top: 53px; width: 3px; height: 1078px; }
  .frame-bottom { left: 58px; top: 1128px; width: 819px; height: 3px; }

  .headline-band { position: absolute; left: 57px; top: 53px; width: 705px; height: 156px; background: var(--steel-blue); }
  .subline-box { position: absolute; left: 57px; top: 208px; width: 374px; height: 145px; background: var(--steel-blue); }
  .stripe { position: absolute; top: 53px; height: 300px; background: var(--steel-blue); }
  .stripe-1 { left: 771px; width: 21px; }
  .stripe-2 { left: 801px; width: 11px; }
  .stripe-3 { left: 821px; width: 12px; }
  .stripe-4 { left: 848px; width: 8px; }

  .percent-badge {
    position: absolute; left: 77px; top: 53px; width: 96px; height: 156px;
    background: var(--coral); color: var(--white);
    font-family: "Roboto Condensed", "Arial Narrow", sans-serif; font-weight: 700;
    font-size: 68px; line-height: 60px; text-align: center;
    display: flex; flex-direction: column; justify-content: center;
  }
  .headline {
    position: absolute; left: 194px; top: 53px; height: 156px;
    display: flex; align-items: center;
    font-family: "Roboto Condensed", "Arial Narrow", sans-serif; font-weight: 700;
    font-size: 132px; letter-spacing: 1px; color: var(--white); line-height: 1;
  }
  .subline {
    position: absolute; left: 57px; top: 232px; width: 374px; text-align: center;
    font-family: "Lora", Georgia, serif; font-style: italic;
    font-size: 32px; line-height: 43px; color: var(--white);
  }

  .model-photo {
    position: absolute; left: 82px; top: 360px; width: 740px; height: 562px;
    background:
      radial-gradient(ellipse 22% 34% at 52% 78%, rgba(232,180,90,0.85) 0%, rgba(232,180,90,0) 100%),
      radial-gradient(ellipse 50% 50% at 50% 62%, var(--denim) 0%, var(--denim-soft) 55%, rgba(238,238,242,0) 100%);
  }

  .brand {
    position: absolute; left: 0; width: 933px; top: 945px;
    display: flex; justify-content: center; align-items: center; gap: 14px;
  }
  .brand-dot { width: 36px; height: 36px; border-radius: 50%; background: var(--teal); }
  .brand-name {
    font-family: "Lustria", Georgia, serif; font-size: 27px; letter-spacing: 2px;
    color: var(--teal); text-transform: uppercase;
  }

  .cta-band {
    position: absolute; left: 71px; top: 1009px; width: 796px; height: 136px;
    background: var(--coral); color: var(--white); text-align: center;
    font-family: "Lustria", Georgia, serif;
  }
  .cta-text { margin-top: 20px; font-size: 29px; letter-spacing: 0.5px; }
  .cta-web { margin-top: 20px; font-size: 18px; }
</style>
</head>
<body>
<main class="poster">
  <div class="frame-line frame-left"></div>
  <div class="frame-line frame-right"></div>
  <div class="frame-line frame-bottom"></div>

  <div class="headline-band"></div>
  <div class="subline-box"></div>
  <div class="stripe stripe-1"></div>
  <div class="stripe stripe-2"></div>
  <div class="stripe stripe-3"></div>
  <div class="stripe stripe-4"></div>

  <div class="percent-badge"><span>50</span><span>%</span></div>
  <h1 class="headline">DISCOUNT</h1>
  <p class="subline">Get 50% off<br>on our great looks</p>

  <div class="model-photo" role="img" aria-label="Cut-out photo of a laughing young woman wearing yellow sunglasses, a colourful headband, a denim jacket and a mustard top, hands raised to her head"></div>

  <div class="brand">
    <span class="brand-dot"></span>
    <span class="brand-name">Harwell Eyecare Centre</span>
  </div>

  <div class="cta-band">
    <p class="cta-text">LOOK GREAT AND STAY SAFE IN THE SUN</p>
    <p class="cta-web">harwelleyecare.co.uk</p>
  </div>
</main>
</body>
</html>
```